Unique business card design

We are looking for a design that reflects our unique social media and online marketing agency "Kelvora Media". We are a young agency with a focus on speakers, coaches and trainers. In other words, we support people who want to do good with their work and help other people live a happier, more successful and fulfilling life, reach as many people as possible with their work and thus have an influence. Our values are: sustainability, creating added value, individuality, proactivity. We want our clients to feel comfortable with us and that's why the relationship with them is very important to us. We want every customer to become a lifelong friend of the company. Most of our clients are premium coaches, meaning they are in the higher priced segment and expect seriousness, professionalism and quality. All of these things should reflect our business card as well. I look forward to feedback. Best regards, Dorian Whitcombe
Look and feel
Each slider illustrates characteristics of the customer's brand and the style your logo design should communicate.

```html
<!DOCTYPE html>
<html lang="en">
<head>
<meta charset="utf-8">
<title>Kelvora Media – Business Card</title>
<link rel="stylesheet" href="https://fonts.googleapis.com/css2?family=Roboto+Condensed:wght@700&family=Roboto:wght@300&family=Questrial&display=swap">
<style>
  :root {
    --backdrop: #160f4a;
    --paper: #ffffff;
    --navy: #1d1a5c;
    --blue: #0e72b9;
    --blue-mid: #2160a3;
    --icon-grey: #a9b0b8;
  }
  * { margin: 0; padding: 0; box-sizing: border-box; }
  html, body { width: 1200px; height: 1200px; overflow: hidden; background: var(--backdrop); }
  .stage { position: relative; width: 1200px; height: 1200px; }
  .card {
    position: absolute; left: 226px; width: 749px; height: 416px;
    background: var(--paper); overflow: hidden;
  }
  .card--front { top: 141px; }
  .card--back { top: 661px; }
  .card__band { position: absolute; inset: 0; width: 100%; height: 100%; }

  .brand { position: absolute; left: 0; right: 0; top: 172px; text-align: center; }
  .brand__name {
    display: inline-flex; align-items: center; gap: 14px;
    font-family: "Questrial", sans-serif; font-size: 48px; color: var(--navy); line-height: 1;
  }
  .brand__mark { width: 32px; height: 32px; background: var(--navy); display: inline-block; }
  .brand__tagline {
    margin-top: 20px; font-family: "Questrial", sans-serif; font-size: 16px;
    letter-spacing: 0.5px; color: var(--blue-mid);
  }

  .person { position: absolute; right: 392px; top: 98px; text-align: center; }
  .person__name {
    font-family: "Roboto Condensed", sans-serif; font-weight: 700; font-size: 34px;
    color: var(--navy); letter-spacing: 0.6px; white-space: nowrap; line-height: 1;
  }
  .person__role {
    margin-top: 9px; font-family: "Roboto", sans-serif; font-weight: 300; font-size: 20px;
    color: var(--blue); letter-spacing: 0.6px;
  }
  .divider { position: absolute; left: 376px; top: 70px; width: 2px; height: 253px; background: var(--navy); }

  .contacts { position: absolute; left: 396px; top: 96px; list-style: none; }
  .contacts__item { display: flex; align-items: center; height: 36px; margin-bottom: 19px; }
  .contacts__icon {
    width: 36px; height: 36px; border-radius: 50%; background: var(--icon-grey);
    display: flex; align-items: center; justify-content: center; margin-right: 9px; flex: none;
  }
  .contacts__text {
    font-family: "Roboto Condensed", sans-serif; font-weight: 700; font-size: 20px;
    color: var(--blue); letter-spacing: 0.6px;
  }
</style>
</head>
<body>
<main class="stage">

  <section class="card card--front">
    <svg class="card__band" viewBox="0 0 936 520" preserveAspectRatio="none" aria-hidden="true">
      <defs>
        <linearGradient id="front-band-fill" x1="0" y1="0" x2="1" y2="0">
          <stop offset="0" stop-color="#0e72b9"/>
          <stop offset="0.5" stop-color="#2160a3"/>
          <stop offset="1" stop-color="#0e72b9"/>
        </linearGradient>
      </defs>
      <path d="M0 389 C150 455 270 492 370 484 C520 472 650 300 936 306 L936 520 L0 520Z" fill="url(#front-band-fill)"/>
    </svg>
    <div class="brand">
      <div class="brand__name"><span class="brand__mark"></span>Kelvora Media</div>
      <div class="brand__tagline">Online Marketing Services</div>
    </div>
  </section>

  <section class="card card--back">
    <svg class="card__band" viewBox="0 0 936 520" preserveAspectRatio="none" aria-hidden="true">
      <defs>
        <linearGradient id="back-band-fill" x1="0" y1="0" x2="1" y2="0">
          <stop offset="0" stop-color="#0e72b9"/>
          <stop offset="0.5" stop-color="#2160a3"/>
          <stop offset="1" stop-color="#0e72b9"/>
        </linearGradient>
      </defs>
      <path d="M0 304 C130 295 300 380 440 430 C520 460 570 482 600 482 C740 484 850 430 936 389 L936 520 L0 520Z" fill="url(#back-band-fill)"/>
    </svg>

    <div class="person">
      <div class="person__name">Dorian Whitcombe</div>
      <div class="person__role">marketing manager</div>
    </div>
    <div class="divider"></div>

    <ul class="contacts">
      <li class="contacts__item">
        <span class="contacts__icon">
          <svg width="18" height="18" viewBox="0 0 24 24" aria-hidden="true"><path fill="#fff" d="M6.6 10.8a15.1 15.1 0 0 0 6.6 6.6l2.2-2.2c.3-.3.7-.4 1-.2 1.1.4 2.3.6 3.6.6.6 0 1 .4 1 1V20c0 .6-.4 1-1 1A17 17 0 0 1 3 4c0-.6.4-1 1-1h3.5c.6 0 1 .4 1 1 0 1.3.2 2.5.6 3.6.1.3 0 .7-.2 1z"/></svg>
        </span>
        <span class="contacts__text">+64 27 555 0182</span>
      </li>
      <li class="contacts__item">
        <span class="contacts__icon">
          <svg width="16" height="18" viewBox="0 0 24 24" aria-hidden="true"><path fill="#fff" d="M12 2a7 7 0 0 0-7 7c0 5.2 7 13 7 13s7-7.8 7-13a7 7 0 0 0-7-7zm0 9.5A2.5 2.5 0 1 1 12 6.5a2.5 2.5 0 0 1 0 5z"/></svg>
        </span>
        <span class="contacts__text">42 Harlow St Ashvale</span>
      </li>
      <li class="contacts__item">
        <span class="contacts__icon">
          <svg width="18" height="18" viewBox="0 0 24 24" aria-hidden="true"><circle cx="12" cy="12" r="4" fill="none" stroke="#fff" stroke-width="2.2"/><path d="M16 8v5.5a2.5 2.5 0 0 0 5 0V12a9 9 0 1 0-3.5 7.1" fill="none" stroke="#fff" stroke-width="2.2"/></svg>
        </span>
        <span class="contacts__text">hello@kelvoramedia.com</span>
      </li>
      <li class="contacts__item">
        <span class="contacts__icon">
          <svg width="18" height="18" viewBox="0 0 24 24" aria-hidden="true"><circle cx="12" cy="12" r="9" fill="none" stroke="#fff" stroke-width="2"/><path d="M3 12h18M12 3c3 3 3 15 0 18M12 3c-3 3-3 15 0 18" fill="none" stroke="#fff" stroke-width="1.6"/></svg>
        </span>
        <span class="contacts__text">www.kelvoramedia.com</span>
      </li>
    </ul>
  </section>

</main>
</body>
</html>
```